Business card required for IT Consultancy Business - Tealbrook Consulting.
Company provides the whole nine yards of services across IT Architecture, design and execution.
Basically we provide consulting services to help businesses make sure their technology is enabling their business strategy.
Design for front and back required.
We would like the front of the card to inlcude:
Name
Title
Mobile number
email address
www.tbkc.com.au
Company logos attached.
Thank you
Industry/Entity Type
Business
Contact Information for Business Card
Name
Title
Mobile number
email address
www.tbkc.com.au
Look and feel
Each slider illustrates characteristics of the customer's brand and the style your logo design should communicate.

```html
<!DOCTYPE html>
<html lang="en">
<head>
<meta charset="utf-8">
<title>Tealbrook Consulting – Business Card</title>
<link href="https://fonts.googleapis.com/css2?family=Montserrat:wght@400;500;600&display=swap" rel="stylesheet">
<style>
  :root {
    --backdrop: #2e2e2e;
    --card-dark: #050505;
    --card-light: #ffffff;
    --brand-blue: #0b76c0;
    --brand-orange: #f05a28;
    --text-grey: #7a7a7a;
    --text-dark: #333333;
    --text-light: #ffffff;
  }
  * { margin: 0; padding: 0; box-sizing: border-box; }
  html, body {
    width: 1200px; height: 864px; overflow: hidden;
    background: var(--backdrop);
    font-family: "Montserrat", sans-serif;
  }
  .canvas { position: relative; width: 1200px; height: 864px; }
  .card {
    position: absolute; width: 560px; height: 320px;
    border-radius: 18px; overflow: hidden;
    box-shadow: 0 12px 28px rgba(0,0,0,.45);
  }

  /* back side */
  .card--back { left: 230px; top: 92px; background: var(--card-dark); }
  .feature-mark {
    position: absolute; left: 34px; top: 40px;
    display: flex; align-items: center; gap: 22px;
  }
  .feature-mark__dot {
    width: 130px; height: 130px; border-radius: 50%;
    background: var(--brand-orange); flex: none;
  }
  .feature-mark__name {
    font-weight: 600; font-size: 40px; line-height: 46px;
    color: var(--brand-blue);
  }
  .wordmark { display: flex; align-items: center; gap: 10px; }
  .wordmark__dot {
    width: 20px; height: 20px; border-radius: 50%;
    background: var(--brand-orange); flex: none;
  }
  .wordmark__name {
    font-weight: 600; color: var(--brand-blue);
    letter-spacing: .3px; white-space: nowrap;
  }
  .card--back .wordmark { position: absolute; right: 40px; bottom: 82px; }
  .card--back .wordmark__name { font-size: 20px; }
  .card--back .web {
    position: absolute; right: 40px; bottom: 56px;
    font-size: 13px; color: var(--text-light); letter-spacing: .5px;
  }

  /* front side */
  .card--front { left: 410px; top: 452px; background: var(--card-light); }
  .card--front .wordmark { position: absolute; left: 34px; top: 168px; }
  .card--front .wordmark__name { font-size: 18px; }
  .divider {
    position: absolute; left: 322px; top: 62px;
    width: 2px; height: 196px; background: var(--brand-blue);
  }
  .details { position: absolute; left: 344px; top: 70px; }
  .details__name { font-size: 22px; font-weight: 600; color: var(--brand-blue); }
  .details__title { font-size: 14px; color: var(--text-grey); margin-top: 2px; }
  .contacts { list-style: none; margin-top: 26px; }
  .contacts li {
    display: flex; align-items: center; gap: 8px;
    font-size: 13px; color: var(--text-dark); line-height: 22px;
  }
  .contacts svg { width: 12px; height: 12px; flex: none; }
</style>
</head>
<body>
<main class="canvas">
  <section class="card card--back" aria-label="Card back">
    <div class="feature-mark">
      <span class="feature-mark__dot"></span>
      <span class="feature-mark__name">Tealbrook<br>Consulting</span>
    </div>
    <div class="wordmark">
      <span class="wordmark__dot"></span>
      <span class="wordmark__name">Tealbrook Consulting</span>
    </div>
    <p class="web">www.tbkc.com.au</p>
  </section>

  <section class="card card--front" aria-label="Card front">
    <div class="wordmark">
      <span class="wordmark__dot"></span>
      <span class="wordmark__name">Tealbrook Consulting</span>
    </div>
    <div class="divider"></div>
    <div class="details">
      <h1 class="details__name">Dana Whitford</h1>
      <p class="details__title">President</p>
      <ul class="contacts">
        <li>
          <svg viewBox="0 0 12 12" aria-hidden="true"><rect x="3" y="0.5" width="6" height="11" rx="1.2" fill="none" stroke="var(--brand-orange)" stroke-width="1.2"/><circle cx="6" cy="9.5" r=".7" fill="var(--brand-orange)"/></svg>
          014-552-3170
        </li>
        <li>
          <svg viewBox="0 0 12 12" aria-hidden="true"><rect x="0.5" y="2" width="11" height="8" fill="var(--brand-orange)"/><path d="M.5 2 6 6.5 11.5 2" fill="none" stroke="#fff" stroke-width="1"/></svg>
          info@tbkc.com.au
        </li>
        <li>
          <svg viewBox="0 0 12 12" aria-hidden="true"><g fill="none" stroke="var(--brand-orange)" stroke-width="1"><circle cx="6" cy="6" r="5.3"/><ellipse cx="6" cy="6" rx="2.4" ry="5.3"/><path d="M.7 6h10.6M1.5 3.5h9M1.5 8.5h9"/></g></svg>
          www.tbkc.com.au
        </li>
      </ul>
    </div>
  </section>
</main>
</body>
</html>
```